" Oferecemos serviço de elaboração de planejamento e orçamento de obras, acompanhamento de reformas, vistorias e elaboração de laudos e pareces, projetos para empreendimentos residenciais e comerciais (fundações, arquitetônico, estrutural, elétrico, hidrossanitário, telecomunicação, gesso, piso, gás, entre outros), consultoria para implantar sistemas de gestão de produtos e processos, análise da viabilidade econômico-financeira, levando em conta estimativa de custos e mercado de trabalho e por fim, administração de obras, incluindo acompanhamento de obras, contratação da mão de obra e controle de orçamento. "

```html
<!DOCTYPE html>
<html lang="pt-BR">
<head>
<meta charset="UTF-8">
<title>Norteva Engenharia — Cartão de Visita</title>
<link rel="stylesheet" href="https://fonts.googleapis.com/css2?family=Exo+2:wght@400;600;800&display=swap">
<style>
  :root {
    --page-bg: #e9ebee;
    --navy-light: #2f5680;
    --navy-dark: #1a3656;
    --teal-edge: #5f9fa6;
    --ink: #1f3a5a;
    --ink-soft: #6b7b8c;
    --card-white: #ffffff;
    --card-grey: #eef0f2;
  }
  * { margin: 0; padding: 0; box-sizing: border-box; }
  html, body {
    width: 1200px; height: 1200px; overflow: hidden;
    background: var(--page-bg);
    font-family: "Exo 2", sans-serif;
  }
  .sheet {
    width: 1200px; height: 1200px;
    display: flex; flex-direction: column;
    align-items: center; justify-content: center; gap: 70px;
  }
  .card {
    width: 900px; height: 500px;
    border-radius: 6px;
    box-shadow: 0 18px 40px rgba(20, 40, 70, 0.18);
    position: relative; overflow: hidden;
  }
  /* Front */
  .card-front {
    background: linear-gradient(135deg, var(--navy-light) 0%, var(--navy-dark) 100%);
    border-bottom: 8px solid var(--teal-edge);
    display: flex; align-items: center; justify-content: center;
  }
  .brand { display: flex; align-items: center; gap: 26px; color: #fff; }
  .brand-mark { width: 22px; height: 22px; background: #fff; }
  .brand-text { display: flex; flex-direction: column; align-items: center; }
  .brand-name {
    font-weight: 800; font-size: 86px; letter-spacing: 4px; line-height: 1;
  }
  .brand-sub {
    font-weight: 800; font-size: 22px; letter-spacing: 17px;
    margin-top: 10px; padding-left: 17px;
  }
  /* Back */
  .card-back {
    background: linear-gradient(180deg, var(--card-white) 0%, var(--card-white) 70%, var(--card-grey) 100%);
    border-bottom: 8px solid var(--teal-edge);
  }
  .back-accent {
    position: absolute; left: 0; top: 70px;
    width: 140px; height: 14px; background: var(--navy-dark);
  }
  .contact {
    position: absolute; left: 420px; top: 110px; color: var(--ink);
  }
  .contact-name { font-weight: 600; font-size: 40px; line-height: 1.1; }
  .contact-role { font-size: 20px; color: var(--ink-soft); margin-top: 4px; }
  .contact-list { list-style: none; margin-top: 46px; }
  .contact-list li {
    display: flex; align-items: center; gap: 14px;
    font-size: 20px; color: var(--ink-soft); margin-bottom: 16px;
  }
  .contact-list svg { width: 20px; height: 20px; flex: none; }
</style>
</head>
<body>
<main class="sheet">
  <section class="card card-front">
    <div class="brand">
      <span class="brand-mark"></span>
      <div class="brand-text">
        <span class="brand-name">NORTEVA</span>
        <span class="brand-sub">ENGENHARIA</span>
      </div>
    </div>
  </section>

  <section class="card card-back">
    <span class="back-accent"></span>
    <div class="contact">
      <p class="contact-name">Nome Sobrenome</p>
      <p class="contact-role">Diretor Comercial</p>
      <ul class="contact-list">
        <li>
          <svg viewBox="0 0 24 24" fill="none" stroke="#1f3a5a" stroke-width="2"><path d="M5 3h4l2 5-3 2a12 12 0 0 0 6 6l2-3 5 2v4a2 2 0 0 1-2 2A17 17 0 0 1 3 5a2 2 0 0 1 2-2z"/></svg>
          (11) 4002-1834
        </li>
        <li>
          <svg viewBox="0 0 24 24" fill="none" stroke="#1f3a5a" stroke-width="2"><rect x="3" y="5" width="18" height="14" rx="2"/><path d="M3 7l9 6 9-6"/></svg>
          contato@norteva.com.br
        </li>
        <li>
          <svg viewBox="0 0 24 24" fill="none" stroke="#1f3a5a" stroke-width="2"><circle cx="12" cy="12" r="9"/><path d="M3 12h18M12 3a14 14 0 0 1 0 18M12 3a14 14 0 0 0 0 18"/></svg>
          www.norteva.com.br
        </li>
      </ul>
    </div>
  </section>
</main>
</body>
</html>
```